Flyer/Poster to promote Bicycle Race

We need a flyer that promotes a bicycle race in downtown Denver. It need to inspire spectators to come watch and bicycle racers to come race. It benefits the Tall Pines Cycling Club is getting urban kids on bikes; sharing healthy lifestyle and values
. We want the colors to be the colors of the logo - blue & red. Community Partnerships must have their logos on the flyer. Flyer must be able to be printed in 8 1/2 x 11 and 11 x 17

Target Market(s)

Neighborhood residents, athletes, cyclists

Industry/Entity Type

Non Profit

Font styles to use
Serif
Sans Serif

Colors
0592cd
ec1f27

Requirements
Must have
• Sunday, July 31, 2016
• Schedule:
• • Racing starts at 7:00am
• • Fun Ride on the Race Course at 12pm
• • Expo & Festival 10am – 6pm
• A Bike Race for Amateurs and Professionals
• A Bike Race for the young, the old & everyone in the middle.
• Great for spectators. Hang out, watch the action & explore the Festival
• Grab a bite to eat & cheer on the racers as they fly around the corners
• Special activities for kids: Wobblo Course, Maple the Moose & More!!
• Renaldo Vasquez KPLT Music Director and Crosstown Groove Hour host will be onsite!
• Start/Finish/Festival will be on Larkwell St between 9th Ave & 11th Ave
• Net proceeds benefit the Tall Pines Cycling Club dedicated to getting urban youth on bikes; sharing healthy lifestyle and values
• Special thanks to the Harrowgate Foundation for their ongoing support
• LARKWELLSTCRIT.COM

```html
<!DOCTYPE html>
<html lang="en">
<head>
<meta charset="utf-8">
<title>The Larkwell St Crit – Sunday, July 31, 2016</title>
<link href="https://fonts.googleapis.com/css2?family=Raleway:wght@400;600;800&display=swap" rel="stylesheet">
<style>
  :root {
    --paper: #ebe8e1;
    --blue: #0592cd;
    --red: #ec1f27;
    --ink: #1d1c24;
    --partner: #8c8c8c;
  }
  * { margin: 0; padding: 0; box-sizing: border-box; }
  html, body { width: 777px; height: 1200px; overflow: hidden; background: var(--paper); }
  .poster {
    position: relative;
    width: 777px; height: 1200px;
    background: var(--paper);
    font-family: "Raleway", sans-serif;
    color: var(--red);
    overflow: hidden;
  }
  .rider {
    position: absolute;
  }
  .rider--blue {
    left: -20px; top: -20px; width: 296px; height: 340px;
    background: radial-gradient(ellipse at 40% 40%, rgba(5,146,205,0.95) 0%, rgba(5,146,205,0.7) 55%, rgba(5,146,205,0) 75%);
  }
  .rider--red {
    left: 505px; top: 720px; width: 290px; height: 410px;
    background: radial-gradient(ellipse at 60% 45%, rgba(236,31,39,0.95) 0%, rgba(236,31,39,0.7) 55%, rgba(236,31,39,0) 75%);
  }
  .brand {
    position: absolute; left: 572px; top: 186px;
    display: flex; align-items: center; gap: 8px;
    font-weight: 800; font-size: 19px; line-height: 1.05;
    color: var(--ink); letter-spacing: 0.5px;
  }
  .brand__mark { width: 12px; height: 12px; background: var(--red); flex: none; }
  .schedule {
    position: absolute; right: 141px; top: 272px;
    text-align: right; font-size: 19px; line-height: 24.5px; font-weight: 400;
  }
  .schedule__title { font-weight: 800; }
  .date {
    position: absolute; left: 96px; top: 384px;
    font-size: 52px; font-weight: 600; color: var(--blue); letter-spacing: 0.2px;
  }
  .point {
    position: absolute; left: 98px; width: 400px;
    font-size: 17px; line-height: 17.6px; font-weight: 400;
  }
  .point--thanks { line-height: 23px; left: 97px; }
  .site {
    position: absolute; left: 97px; top: 1098px;
    font-size: 13px; font-weight: 400; letter-spacing: 0.2px;
  }
  .partners {
    position: absolute; left: 86px; top: 1143px; width: 610px; height: 36px;
    display: flex; justify-content: space-between; align-items: center;
  }
  .partner { background: var(--partner); opacity: 0.75; }
  .partner--wide { width: 42px; height: 20px; }
  .partner--square { width: 26px; height: 26px; }
  .partner--round { width: 26px; height: 26px; border-radius: 50%; }
</style>
</head>
<body>
<main class="poster">
  <div class="rider rider--blue" role="img" aria-label="Blue silhouette of a racing cyclist riding in from the top left corner"></div>
  <div class="rider rider--red" role="img" aria-label="Red silhouette of a racing cyclist leaning into a corner at the bottom right"></div>

  <div class="brand"><span class="brand__mark"></span><span>THE LARKWELL ST<br>CRIT</span></div>

  <section class="schedule">
    <p class="schedule__title">Schedule:</p>
    <p>7:00am - Race Starts</p>
    <p>12pm - Fun Ride on the Race Course</p>
    <p>10am – 6pm - Expo &amp; Festival</p>
  </section>

  <h1 class="date">Sunday, July 31, 2016</h1>

  <p class="point" style="top:478px">A Bike Race for Amateurs and Professionals</p>
  <p class="point" style="top:513px">A Bike Race for the young, the old &amp;<br>everyone in the middle</p>
  <p class="point" style="top:566px">Great for spectators. Hang out, watch the<br>action &amp; explore the Festival</p>
  <p class="point" style="top:619px">Grab a bite to eat &amp; cheer on the racers as<br>they fly around the corners</p>
  <p class="point" style="top:672px">Special activities for kids: Wobblo Course,<br>Maple the Moose &amp; More</p>
  <p class="point" style="top:725px">Renaldo Vasquez KPLT Music Director and<br>Crosstown Groove Hour host will be onsite</p>
  <p class="point" style="top:778px">Start/Finish/Festival will be on Larkwell St<br>between 9th Ave &amp; 11th Ave</p>
  <p class="point" style="top:831px">Net proceeds benefit the Tall Pines<br>Cycling Club dedicated to getting urban<br>youth on bikes; sharing healthy lifestyle<br>and values</p>
  <p class="point point--thanks" style="top:917px">Special thanks to the Harrowgate Foundation<br>for their ongoing support</p>

  <p class="site">LARKWELLSTCRIT.COM</p>

  <div class="partners" aria-label="Community partners">
    <span class="partner partner--wide"></span>
    <span class="partner partner--wide"></span>
    <span class="partner partner--round"></span>
    <span class="partner partner--wide"></span>
    <span class="partner partner--square"></span>
    <span class="partner partner--square"></span>
    <span class="partner partner--wide"></span>
    <span class="partner partner--wide"></span>
    <span class="partner partner--round"></span>
    <span class="partner partner--wide"></span>
  </div>
</main>
</body>
</html>
```